Verpackungen für drei Naturheilprodukte und ein Verkaufsdisplay
Zielgruppe
Wir sind ein Team von drei Personen die sich das Ziel gesetzt haben möglichst viele Personen mit den Wirkstoffen aus der Natur zu erreichen. Wir sind der Überzeugung, dass die Wirkstoffe der Natur vorbeugend schlimmeres verhindern kann und auch auf sanfte Art und Weise dem Körber die Natürliche Energie zurückgeben kann.
Die Produkte werden laufend erweitert somit wird auch auf eine zukünftige Zusammenarbeit Wert gelegt.
Momentan arbeiten wir an folgenden Produkten die verpackt werden müssen:
- Bachblüten/CBD Globuli:
Diese wirken beruhigend, angstlösend stresslindernd. Die Verpackung wird aus einem Faltkarton sein (40mm x 35mm x 80mm)
- Hautpflege Salbe
Diese ist auch auf CBD und Kamillenblüten Basis. Diese wirkt entzündungshemmend, beschleunigt und unterstützt den Heilungsprozess. Die Creme ist in einem 30ml Glass.
- CBD Blüten (legales Cannabis).
Dies wirkt besonders Schmerzlindernd, krampflösend und entzündungshemmend. Die momentan verkaufte Sorte der Hanfblüte ist CBD Lumaris ca. 16% CBD/0,6% Gehalt THC (diese Angaben sollten einfach zu wechseln sein). Die Verpackung wird aus einem Faltkarton sein (ca. 60mm x 50mm x 80mm, für andere Vorschläge offen).
- Weiter stelle ich mir ein Ausstellungsdisplay vor. So Kompakt wie möglich, damit es gut auf dem Verkaufstresen platzfindet, jedoch trotzdem ins Auge sticht.
Aufgabenstellung
Sie Designen hier unsere Produktelinie momentan bestehend aus drei Produkten. Diese sollten ein einheitliches erscheinen und ein edles und schlichtes auftreten haben. Nicht Hanflastig. Das Hauptaugenmerk sollte eher auf Wellness, Gesundheit und Natur gesetzt sein. Den Rest lasse ich mich auf die Kreativität der Designer überraschen

```html
<!DOCTYPE html>
<html lang="de">
<head>
<meta charset="utf-8">
<title>Verdalis – CBD Blüten Faltschachtel</title>
<link href="https://fonts.googleapis.com/css2?family=Tinos:ital,wght@0,400;0,700;1,400&family=Open+Sans:wght@400&display=swap" rel="stylesheet">
<style>
  :root{
    --green:#036649;
    --lime:#8db810;
    --ink:#444;
    --line:#8a8a8a;
    --paper:#fff;
  }
  *{box-sizing:border-box;margin:0;padding:0}
  html,body{width:681px;height:1200px;overflow:hidden;background:var(--paper)}
  body{position:relative;font-family:"Tinos",serif;color:var(--ink)}
  .spec-label{position:absolute;left:24px;top:41px;font-family:"Open Sans",sans-serif;font-size:5.6px;letter-spacing:.6px;color:#666}
  .sheet{position:absolute;left:0;width:681px;height:530px}
  .sheet--one{top:65.5px}
  .sheet--two{top:589.5px}
  .dieline{position:absolute;left:0;top:0}
  .band{position:absolute;left:48.6px;top:166.5px;width:583.7px;height:4.7px;background:var(--lime)}
  .panel{position:absolute;top:171.2px;height:190px;width:145.9px;font-size:4.3px;line-height:5.7px}
  .panel p{margin-bottom:3.8px;text-align:justify}
  .panel b{font-weight:700}
  .panel--story{left:48.6px;background:var(--green);color:#fff;padding:0 8px}
  .panel--info{left:194.5px;padding:12.6px 8px 0}
  .panel--front{left:340.4px}
  .panel--care{left:486.4px;padding:12.6px 8px 0}
  .brand{position:absolute;left:0;width:100%;text-align:center}
  .brand__mark{display:block;margin:0 auto;width:30px;height:30px;border-radius:50%}
  .brand__name{display:block;font-size:17px;line-height:18px;margin-top:6px}
  .panel--story .brand{top:10px;color:#fff}
  .panel--story .brand__mark{background:var(--lime)}
  .story-text{position:absolute;left:8px;right:8px;top:77px}
  .benefits{list-style:none;margin-top:4px}
  .benefits li{position:relative;padding-left:6px}
  .benefits li::before{content:"";position:absolute;left:0;top:1.8px;width:2.4px;height:2.4px;border-radius:50%;background:var(--lime)}
  .maker{position:absolute;left:10px;top:163px;line-height:5.7px}
  .seals{position:absolute;right:7px;top:164px;display:flex;gap:4px;align-items:center}
  .seal{width:14px;height:14px;border-radius:50%;border:1px solid #fff}
  .seal--square{border-radius:1px;width:12px;height:12px}
  .icons{position:absolute;left:0;top:127px;width:100%}
  .icon{position:absolute;width:22.5px;text-align:center;transform:translateX(-50%)}
  .icon__ring{width:22.5px;height:22.5px;border-radius:50%;border:.8px solid var(--ink);display:flex;align-items:center;justify-content:center;font-size:8px;font-weight:700}
  .icon__label{width:34px;margin-left:-5.75px;margin-top:3px;font-size:4.1px;line-height:5px}
  .made-in{position:absolute;left:8px;top:175px;font-weight:700}
  .panel--front .brand{top:9px;color:var(--ink)}
  .panel--front .brand__mark{background:var(--green)}
  .front-field{position:absolute;left:0;top:76px;width:100%;height:114px;background:var(--green);border-top:2.4px solid var(--lime);color:#fff}
  .product-title{position:absolute;left:16px;top:12px;width:113.5px;font-size:13.5px;line-height:16px;border-bottom:1px solid #fff;padding-bottom:1px}
  .product-strain{position:absolute;left:16px;top:38px;font-size:9.4px}
  .product-dose{position:absolute;left:16px;top:51px;font-size:7.6px}
  .product-claim{position:absolute;left:16px;top:68px;font-size:6px;line-height:8.6px;font-style:italic}
  .product-weight{position:absolute;left:16px;top:97px;font-size:5.6px}
  .product-weight span{font-size:9px}
  .front-badges{position:absolute;right:15px;top:87px;display:flex;gap:4px}
  .front-badges--top{top:14px;right:16px}
  .front-badge{width:16.5px;height:16.5px;border-radius:50%;border:.9px solid #fff;display:flex;align-items:center;justify-content:center;font-size:5.6px;font-weight:700}
  .best-before{position:absolute;left:8px;top:170px}
  .flap-web{position:absolute;left:340.5px;width:146px;top:90px;text-align:center;font-size:5.4px;letter-spacing:.3px;color:var(--green)}
  .lot{position:absolute;left:94.5px;top:439px;font-size:5.4px;letter-spacing:.4px;line-height:14px}
  .lot__row{display:flex;align-items:center}
  .lot__key{width:26px}
</style>
</head>
<body>
<div class="spec-label">PACKAGING 90 MM x 90 MM x 120 MM</div>

<section class="sheet sheet--one">
  <svg class="dieline" width="681" height="530" viewBox="0 0 681 530" fill="none" stroke="#8a8a8a" stroke-width=".5">
    <path d="M340.5,166.5 V15 Q340.5,1.4 354,1.4 H473 Q486.4,1.4 486.4,15 V166.5"/>
    <line x1="340.5" y1="20" x2="486.4" y2="20"/>
    <path d="M194.6,166.5 V129 L198.3,122 L202,43.5 H337.2 L340.5,166.5"/>
    <path d="M486.4,166.5 L489.2,43.5 H624.4 L628.1,74.8 L632.3,83.2 V166.5"/>
    <path d="M194.6,361 L198.3,368 L202,484 H337.2 L338.5,361"/>
    <path d="M488.4,361 L489.2,484 H624.4 L628.1,372 L632.3,366 V361"/>
    <path d="M48.6,361 V512 Q48.6,526 62,526 H181 Q194.6,526 194.6,512 V361"/>
    <line x1="48.6" y1="507" x2="194.6" y2="507"/>
    <rect x="48.6" y="166.5" width="583.7" height="194.7"/>
  </svg>
  <div class="flap-web">www.verdalis.example</div>
  <div class="band"></div>

  <div class="panel panel--story">
    <div class="brand"><span class="brand__mark"></span><span class="brand__name">Verdalis</span></div>
    <div class="story-text">
      <p>Natürlich Kuren mit der ganzen, natürlichen Pflanze für Ihr persönliches Wohlbefinden.</p>
      <p>Lorem ipsum dolor sit amet, consetetur sadipscing elitr, sed diam nonumy eirmod tempor invidunt ut labore et dolore magna aliquyam erat, sed diam voluptua. At vero eos et accusam et justo duo dolores. Lorem ipsum dolor sit amet. Lorem ipsum dolor sit amet, consetetur sadipscing elitr, sed diam nonumy eirmod tempor invidunt ut labore et dolore magna.</p>
      <ul class="benefits">
        <li>Schmerzlindernd, krapflösend &amp; entzündungshemmend</li>
        <li>Glutenfrei, lactosefrei, fructosefrei, vegan</li>
        <li>Großpackung für ein halbes Jahr</li>
      </ul>
    </div>
    <div class="maker">Verdalis GmbH<br>D-12345 Musterstadt<br>www.verdalis.example</div>
    <div class="seals"><span class="seal seal--square"></span><span class="seal"></span></div>
  </div>

  <div class="panel panel--info">
    <p><b>Verzehrempfehlung:</b><br>Lorem ipsum dolor sit amet, consetetur sadipscing elitr, sed diam nonumy eirmod tempor invidunt ut labore et dolore magna aliquyam erat, sed diam voluptua.</p>
    <p><b>Inhaltsstoffe:</b> Lorem ipsum dolor sit amet, consetetur sadipscing elitr, sed diam nonumy eirmod tempor invidunt ut labore et dolore magna aliquyam erat, sed diam voluptua. At vero eos et accusam et justo duo dolores et ea rebum. Stet clita kasd gubergren, no sea takimata sanctus est Lorem ipsum dolor sit amet. Lorem ipsum dolor sit amet, consetetur sadipscing elitr, sed diam nonumy eirmod tempor invidunt ut labore et dolore magna aliquyam erat.</p>
    <p style="text-align:left">*% der empfohlenen Tagesdosis in der EU / Recommended daily intake according to the EU<br>Weitere Inhaltsstoffe / Other Ingredients: Hydroxypropylmethylcellulose (Kapselhülle / Caspsule Cover), Magnesiumstearat (Trennmittel/release agent)</p>
    <div class="icons">
      <div class="icon" style="left:34.6px"><div class="icon__ring">Bio</div><div class="icon__label">Kontrolliert biologisch</div></div>
      <div class="icon" style="left:73px"><div class="icon__ring">18+</div><div class="icon__label">Keine Abgabe unter 18 Jahren</div></div>
      <div class="icon" style="left:111.4px"><div class="icon__ring"></div><div class="icon__label">Nicht zum Verzehr geeignet</div></div>
    </div>
    <div class="made-in">Hergestellt in Deutschland</div>
  </div>

  <div class="panel panel--front">
    <div class="brand"><span class="brand__mark"></span><span class="brand__name">Verdalis</span></div>
    <div class="front-field">
      <div class="product-title">CBD Blüten</div>
      <div class="product-strain">(CBD Lumaris)</div>
      <div class="product-dose">16% CBD / 0,6% THC</div>
      <div class="product-claim">Schmerzlindernd, krampflösend &amp;<br>entzündungshemmend</div>
      <div class="product-weight">10 g <span>℮</span></div>
      <div class="front-badges"><span class="front-badge">18+</span><span class="front-badge"></span></div>
    </div>
  </div>

  <div class="panel panel--care">
    <p><b>Verzehrempfehlung:</b> Erwachsene verzehren täglich morgens 1-2 Kapseln mit ausreichend Flüssigkeit und einem Snack. / Suggested Use: Adults take 1-2 capsules with sufficient liquid and a carbohydrate snack preferably in the morning.</p>
    <p style="text-align:left"><b>Aufbewahrung:</b> Vor Wärme und Feuchtigkeit schützen. Außerhalb der Reichweite von kleinen Kindern aufbewahren. / Store in a cool, dry place.</p>
    <p><b>Hinweise:</b> Die angegebene empfohlene tägliche Verzehrmenge darf nicht überschritten werden. Sprechen Sie stets mit Ihrem Arzt, bevor Sie Nahrungsergänzungsmittel einnehmen. Nahrungsergänzungsmittel sollten nicht als Ersatz für eine ausgewogene und abwechslungsreiche Ernährung verwendet werden. Enthält Koffein, für Kinder und schwangere Frauen nicht empfohlen. / Caution: Do not exceed recommended dosage. Consult your GP before taking Food supplements. Should not be used as a substitute for balanced and varied diet. Contains caffeine, not recommended for children and pregnant women.</p>
    <div class="best-before">Mindestens haltbar bis:<br>Siehe Boden</div>
  </div>

  <div class="lot">
    <div class="lot__row"><span class="lot__key">LOT:</span>18AA072GH</div>
    <div class="lot__row"><span class="lot__key"><svg width="6" height="9" viewBox="0 0 6 9"><rect x=".3" y=".3" width="5.4" height="8.4" fill="none" stroke="#444" stroke-width=".6"/><path d="M1 5 H5 V8.4 H1Z" fill="#444"/></svg></span>03 / 2022</div>
  </div>
</section>

<section class="sheet sheet--two">
  <svg class="dieline" width="681" height="530" viewBox="0 0 681 530" fill="none" stroke="#8a8a8a" stroke-width=".5">
    <path d="M340.5,166.5 V15 Q340.5,1.4 354,1.4 H473 Q486.4,1.4 486.4,15 V166.5"/>
    <line x1="340.5" y1="20" x2="486.4" y2="20"/>
    <path d="M194.6,166.5 V129 L198.3,122 L202,43.5 H337.2 L340.5,166.5"/>
    <path d="M486.4,166.5 L489.2,43.5 H624.4 L628.1,74.8 L632.3,83.2 V166.5"/>
    <path d="M194.6,361 L198.3,368 L202,484 H337.2 L338.5,361"/>
    <path d="M488.4,361 L489.2,484 H624.4 L628.1,372 L632.3,366 V361"/>
    <path d="M48.6,361 V512 Q48.6,526 62,526 H181 Q194.6,526 194.6,512 V361"/>
    <line x1="48.6" y1="507" x2="194.6" y2="507"/>
    <rect x="48.6" y="166.5" width="583.7" height="194.7"/>
  </svg>
  <div class="flap-web">www.verdalis.example</div>
  <div class="band"></div>

  <div class="panel panel--story">
    <div class="brand"><span class="brand__mark"></span><span class="brand__name">Verdalis</span></div>
    <div class="story-text">
      <p>Natürlich Kuren mit der ganzen, natürlichen Pflanze für Ihr persönliches Wohlbefinden.</p>
      <p>Lorem ipsum dolor sit amet, consetetur sadipscing elitr, sed diam nonumy eirmod tempor invidunt ut labore et dolore magna aliquyam erat, sed diam voluptua. At vero eos et accusam et justo duo dolores. Lorem ipsum dolor sit amet. Lorem ipsum dolor sit amet, consetetur sadipscing elitr, sed diam nonumy eirmod tempor invidunt ut labore et dolore magna.</p>
      <ul class="benefits">
        <li>Schmerzlindernd, krapflösend &amp; entzündungshemmend</li>
        <li>Glutenfrei, lactosefrei, fructosefrei, vegan</li>
        <li>Großpackung für ein halbes Jahr</li>
      </ul>
    </div>
    <div class="maker">Verdalis GmbH<br>D-12345 Musterstadt<br>www.verdalis.example</div>
    <div class="seals"><span class="seal seal--square"></span><span class="seal"></span></div>
  </div>

  <div class="panel panel--info">
    <p><b>Verzehrempfehlung:</b><br>Lorem ipsum dolor sit amet, consetetur sadipscing elitr, sed diam nonumy eirmod tempor invidunt ut labore et dolore magna aliquyam erat, sed diam voluptua.</p>
    <p><b>Inhaltsstoffe:</b> Lorem ipsum dolor sit amet, consetetur sadipscing elitr, sed diam nonumy eirmod tempor invidunt ut labore et dolore magna aliquyam erat, sed diam voluptua. At vero eos et accusam et justo duo dolores et ea rebum. Stet clita kasd gubergren, no sea takimata sanctus est Lorem ipsum dolor sit amet. Lorem ipsum dolor sit amet, consetetur sadipscing elitr, sed diam nonumy eirmod tempor invidunt ut labore et dolore magna aliquyam erat.</p>
    <p style="text-align:left">*% der empfohlenen Tagesdosis in der EU / Recommended daily intake according to the EU<br>Weitere Inhaltsstoffe / Other Ingredients: Hydroxypropylmethylcellulose (Kapselhülle / Caspsule Cover), Magnesiumstearat (Trennmittel/release agent)</p>
    <div class="icons">
      <div class="icon" style="left:34.6px"><div class="icon__ring">Bio</div><div class="icon__label">Kontrolliert biologisch</div></div>
      <div class="icon" style="left:73px"><div class="icon__ring">18+</div><div class="icon__label">Keine Abgabe unter 18 Jahren</div></div>
      <div class="icon" style="left:111.4px"><div class="icon__ring"></div><div class="icon__label">Nicht zum Verzehr geeignet</div></div>
    </div>
    <div class="made-in">Hergestellt in Deutschland</div>
  </div>

  <div class="panel panel--front">
    <div class="brand"><span class="brand__mark"></span><span class="brand__name">Verdalis</span></div>
    <div class="front-field">
      <div class="product-title">CBD Blüten</div>
      <div class="front-badges front-badges--top"><span class="front-badge"></span></div>
      <div class="product-strain">(CBD Lumaris)</div>
      <div class="product-dose">16% CBD / 0,6% THC</div>
      <div class="product-claim">Schmerzlindernd, krampflösend &amp;<br>entzündungshemmend</div>
      <div class="product-weight">10 g <span>℮</span></div>
    </div>
  </div>

  <div class="panel panel--care">
    <p><b>Verzehrempfehlung:</b> Erwachsene verzehren täglich morgens 1-2 Kapseln mit ausreichend Flüssigkeit und einem Snack. / Suggested Use: Adults take 1-2 capsules with sufficient liquid and a carbohydrate snack preferably in the morning.</p>
    <p style="text-align:left"><b>Aufbewahrung:</b> Vor Wärme und Feuchtigkeit schützen. Außerhalb der Reichweite von kleinen Kindern aufbewahren. / Store in a cool, dry place.</p>
    <p><b>Hinweise:</b> Die angegebene empfohlene tägliche Verzehrmenge darf nicht überschritten werden. Sprechen Sie stets mit Ihrem Arzt, bevor Sie Nahrungsergänzungsmittel einnehmen. Nahrungsergänzungsmittel sollten nicht als Ersatz für eine ausgewogene und abwechslungsreiche Ernährung verwendet werden. Enthält Koffein, für Kinder und schwangere Frauen nicht empfohlen. / Caution: Do not exceed recommended dosage. Consult your GP before taking Food supplements. Should not be used as a substitute for balanced and varied diet. Contains caffeine, not recommended for children and pregnant women.</p>
    <div class="best-before">Mindestens haltbar bis:<br>Siehe Boden</div>
  </div>

  <div class="lot">
    <div class="lot__row"><span class="lot__key">LOT:</span>18AA072GH</div>
    <div class="lot__row"><span class="lot__key"><svg width="6" height="9" viewBox="0 0 6 9"><rect x=".3" y=".3" width="5.4" height="8.4" fill="none" stroke="#444" stroke-width=".6"/><path d="M1 5 H5 V8.4 H1Z" fill="#444"/></svg></span>03 / 2022</div>
  </div>
</section>
</body>
</html>
```